TovaLamishpacha - Israeli Mental Health Website

We are developing an Israeli website for mental health. The website will be both in English and in Hebrew. We have a logo and would like a website design based on the logo and the logos colors (attached).

Attached is a doc that contains the website requirements.

We would like to have an icon for each of the sidebar categories, an image for each of the pages (including each of the sidebar category pages).

Target Market(s)

Adults 18-80

Industry/Entity Type

Mental Health

Number of Pages Required

5+ page

Font styles to use
Sans Serif

Colors

Designer to choose colors to be used in the design.

```html
<!DOCTYPE html>
<html lang="en">
<head>
<meta charset="utf-8">
<title>TovaLamishpacha – Mental Health</title>
<link href="https://fonts.googleapis.com/css2?family=Poppins:wght@400;500;600;700;800&display=swap" rel="stylesheet">
<style>
:root{
  --blue:#1f6fbf;
  --blue-dark:#185fa6;
  --green:#4ca23c;
  --green-dark:#3f8f31;
  --ink:#1f2a33;
  --text:#4b5560;
  --grey-bg:#f5f5f5;
  --line:#e6e6e6;
  --white:#ffffff;
}
*{box-sizing:border-box;margin:0;padding:0}
html,body{width:1200px;height:3996px;overflow:hidden}
body{font-family:'Poppins',sans-serif;color:var(--ink);background:var(--white);position:relative}
.abs{position:absolute}
a{text-decoration:none;color:inherit}

/* header */
.topbar{position:absolute;left:0;top:0;width:1200px;height:75px;background:var(--white)}
.brand{position:absolute;left:88px;top:20px;display:flex;align-items:center;gap:10px;font-weight:700;font-size:24px;color:var(--blue)}
.brand .dot{width:34px;height:34px;border-radius:50%;background:var(--green)}
.contact{position:absolute;top:20px;display:flex;align-items:center;gap:12px}
.contact .ic{width:34px;height:34px;border-radius:50%;background:#eaf4e7;display:flex;align-items:center;justify-content:center}
.contact small{display:block;font-size:10px;color:#8a8f95}
.contact b{display:block;font-size:16px;font-weight:600;color:var(--ink);line-height:1.1}
.lang{position:absolute;left:1028px;top:30px;font-size:12px;font-weight:500;display:flex;align-items:center;gap:8px}
.lang .flag{width:16px;height:10px;background:linear-gradient(#2d5bb4 0 50%,#e04040 50%)}

.navbar{position:absolute;left:0;top:75px;width:1200px;height:41px;background:var(--blue)}
.cat-head{position:absolute;left:88px;top:75px;width:317px;height:41px;background:var(--green);color:#fff;font-weight:700;font-size:14px;padding:0 22px;display:flex;align-items:center;justify-content:space-between}
.menu{position:absolute;left:434px;top:75px;height:41px;display:flex;align-items:center;gap:32px;color:#fff;font-size:12px;font-weight:600}

/* hero */
.hero-bg{position:absolute;left:0;top:116px}
.hero-photo{position:absolute;left:700px;top:116px;width:500px;height:730px}
.hero-text{position:absolute;left:470px;top:276px;color:#fff}
.kicker{display:flex;align-items:center;gap:14px;font-size:13px;font-weight:600;letter-spacing:.3px}
.kicker i{display:block;width:34px;height:2px;background:#fff}
.hero-text h1{font-size:88px;line-height:84px;font-weight:800;margin-top:10px}
.btn-ghost{position:absolute;left:472px;top:497px;width:189px;height:40px;border:2px solid #fff;border-radius:20px;color:#fff;font-size:12px;font-weight:700;display:flex;align-items:center;justify-content:center}
.dots{position:absolute;left:473px;top:646px;display:flex;gap:8px}
.dots span{width:12px;height:12px;border-radius:50%;border:2px solid #fff}
.dots span.on{background:#fff}

/* sidebar */
.sidebar{position:absolute;left:88px;top:116px;width:317px;height:686px;background:#fff;border-radius:0 0 12px 12px;box-shadow:0 8px 24px rgba(0,0,0,.08);padding:8px 18px 0}
.sidebar li{list-style:none;height:51.6px;display:flex;align-items:center;border-bottom:1px solid var(--line);font-size:12px;color:var(--ink)}
.sidebar li:last-child{border-bottom:none}
.sidebar .cic{width:30px;height:30px;border:2px solid var(--green);border-radius:50%;margin:0 12px 0 4px;flex:none}
.sidebar .chev{margin-left:auto;font-size:14px;font-weight:600}

/* about */
.about-bg{position:absolute;left:0;top:846px}
.photo-circle{position:absolute;border-radius:50%}
.section-kicker{display:flex;align-items:center;gap:12px;font-size:13px;font-weight:600;color:var(--blue)}
.section-kicker i{display:block;width:36px;height:2px;background:var(--blue)}
.about{position:absolute;left:705px;top:935px;width:356px}
.about h2{font-size:42px;font-weight:700;color:var(--blue);margin-top:6px}
.about p{font-size:13px;line-height:20.5px;color:var(--text);margin-top:10px}
.btn-green{display:inline-flex;align-items:center;justify-content:center;width:142px;height:39px;border-radius:20px;background:var(--green);color:#fff;font-size:12px;font-weight:700;margin-top:22px}

/* services */
.services-title{position:absolute;left:0;top:1468px;width:1200px;text-align:center}
.services-title h2{font-size:42px;font-weight:700;color:var(--blue)}
.services-title p{font-size:13px;color:var(--text);margin-top:2px}
.card{position:absolute;top:1575px;width:439px;height:466px;background:#fff;border-radius:18px;box-shadow:0 10px 30px rgba(0,0,0,.08);overflow:hidden}
.card .img{height:264px}
.card .body{padding:30px 28px}
.card h3{font-size:20px;font-weight:600}
.card p{font-size:12.5px;line-height:19.5px;color:var(--text);margin-top:14px}
.link{display:inline-block;font-size:11.5px;font-weight:700;color:var(--green);text-decoration:underline;margin-top:18px}

/* therapists */
.feature{position:absolute;width:380px}
.feature h3{font-size:20px;font-weight:600}
.feature p{font-size:13px;line-height:19.8px;color:var(--text);margin-top:14px}
.feature.on-green h3,.feature.on-green p,.feature.on-green .link{color:#fff}

.play{position:absolute;left:586px;top:3548px;width:100px;height:100px;border-radius:50%;background:var(--green);display:flex;align-items:center;justify-content:center}

/* footer */
.footer-bg{position:absolute;left:0;top:3640px}
.footer-brand{position:absolute;left:0;top:3852px;width:1200px;display:flex;justify-content:center;align-items:center;gap:12px;color:#fff;font-size:30px;font-weight:700}
.footer-brand .dot{width:44px;height:44px;border-radius:50%;border:3px solid #fff}
.footer-line{position:absolute;left:88px;top:3934px;width:1024px;height:1px;background:rgba(255,255,255,.35)}
.footer-copy{position:absolute;left:425px;top:3964px;color:#fff;font-size:12px;font-weight:600}
.footer-links{position:absolute;left:945px;top:3964px;color:#fff;font-size:12px;font-weight:600;display:flex;gap:14px}
.chat-float{position:absolute;left:1134px;top:3920px;width:44px;height:44px;border-radius:50%;background:#25c25a;display:flex;align-items:center;justify-content:center}
</style>
</head>
<body>

<!-- header -->
<header class="topbar">
  <div class="brand"><span class="dot"></span>TovaLamishpacha</div>
  <div class="contact" style="left:566px">
    <span class="ic"><svg width="14" height="11" viewBox="0 0 14 11"><rect x="1" y="1" width="12" height="9" rx="1" fill="none" stroke="#4ca23c" stroke-width="1.6"/><path d="M1 1l6 5 6-5" fill="none" stroke="#4ca23c" stroke-width="1.6"/></svg></span>
    <div><small>Email:</small><b>info@example.com</b></div>
  </div>
  <div class="contact" style="left:817px">
    <span class="ic"><svg width="14" height="14" viewBox="0 0 14 14"><path d="M3 1l2.5 3-1.5 1.5c.8 1.8 2.2 3.2 4 4L9.5 8 12.5 10.5 11 13C5.5 12.5 1.5 8.5 1 3z" fill="#4ca23c"/></svg></span>
    <div><small>Call Us:</small><b>+123-456-789</b></div>
  </div>
  <div class="lang"><span class="flag"></span>English <span>⌄</span></div>
</header>

<nav class="navbar"></nav>
<div class="cat-head"><span>CATEGORIES</span><span>⌄</span></div>
<div class="menu">
  <span>SMART CHATLINE</span><span>THERAPISTS</span><span>ORGANIZATIONS</span><span>VIDEOS</span><span>CONTACT</span><span>ABOUT</span><span>DONATE</span>
</div>

<!-- hero -->
<svg class="hero-bg" width="1200" height="730" viewBox="0 0 1200 730">
  <defs><linearGradient id="heroGrad" x1="0" y1="0" x2="1" y2="0"><stop offset="0" stop-color="#c9c6c2"/><stop offset="1" stop-color="#d8d3cc"/></linearGradient></defs>
  <path d="M0 0H1200V720C1080 740 980 650 880 690 780 730 700 600 560 560 420 520 300 640 160 620 80 610 30 560 0 520Z" fill="url(#heroGrad)"/>
</svg>
<div class="hero-photo" role="img" aria-label="Woman in distress holding her head while talking with a counsellor" style="background:linear-gradient(135deg,#e3ded6 0%,#c98f3c 45%,#8a6a4a 75%,#3a342e 100%);clip-path:path('M0 0H500V700C430 740 330 720 230 680 160 650 90 620 0 600Z')"></div>
<div class="hero-text">
  <div class="kicker"><i></i>WELCOME TO</div>
  <h1>Mental<br>Health</h1>
</div>
<a class="btn-ghost">MAKE AN APOINTMENT</a>
<div class="dots"><span></span><span class="on"></span><span></span></div>

<!-- sidebar -->
<ul class="sidebar">
  <li><span class="cic"></span>Emergency Mental Help<span class="chev">›</span></li>
  <li><span class="cic"></span>Suicide<span class="chev">›</span></li>
  <li><span class="cic"></span>Sexual Assault/Violence Victims<span class="chev">›</span></li>
  <li><span class="cic"></span>Sexual Assault/Violence Assaulters<span class="chev">›</span></li>
  <li><span class="cic"></span>Post Trauma<span class="chev">›</span></li>
  <li><span class="cic"></span>Depression<span class="chev">›</span></li>
  <li><span class="cic"></span>Anxiety<span class="chev">›</span></li>
  <li><span class="cic"></span>Addictions<span class="chev">›</span></li>
  <li><span class="cic"></span>Sleep Disorders<span class="chev">›</span></li>
  <li><span class="cic"></span>Eating Disorders<span class="chev">›</span></li>
  <li><span class="cic"></span>Financial Problems<span class="chev">›</span></li>
  <li><span class="cic"></span>Parenthood<span class="chev">›</span></li>
  <li><span class="cic"></span>Relationship<span class="chev">›</span></li>
</ul>

<!-- about -->
<svg class="about-bg" width="1200" height="760" viewBox="0 0 1200 760">
  <path d="M0 0C60 60 140 20 160 0H1200V480C1080 420 960 440 860 490 760 540 650 540 560 470 420 360 200 520 0 720Z" fill="#f6f6f6"/>
</svg>
<div class="photo-circle" role="img" aria-label="Counsellor comforting a woman covering her face" style="left:134px;top:879px;width:464px;height:464px;background:radial-gradient(circle at 45% 40%,#d9b8a6,#8f7a6a 55%,#6b6f74)"></div>
<div class="photo-circle" role="img" aria-label="Man sitting on a sofa with his head in his hands" style="left:426px;top:1128px;width:218px;height:218px;border:6px solid #fff;background:radial-gradient(circle at 50% 40%,#b8b5b0,#7c8591 60%,#55606c)"></div>
<div class="about">
  <div class="section-kicker"><i></i>ABOUT US</div>
  <h2>Mental Health</h2>
  <p>Aenean sollicitudin, lorem quis bibendum auctor, nisi elit consequat ipsum, nec sagittis sem nibh id elit. Duis sed odio sit amet nibh vulputate cursus a sit amet mauris. Morbi accumsan ipsum velit. Nam nec tellus a odio tincidunt auctor a ornare odio. Sed non mauris vitae erat consequat auctor eu in elit. Class aptent taciti sociosqu ad litora torquent per conubia nostra, per inceptos himenaeos. Mauris in erat justo. Nullam ac urna eu felis dapibus condimentum sit amet a augue. Sed non neque elit.</p>
  <a class="btn-green">FIND OUT MORE</a>
</div>

<!-- services -->
<div class="services-title">
  <h2>Our Services</h2>
  <p>Mental haelth and behavioral health best services</p>
</div>
<article class="card" style="left:146px">
  <div class="img" role="img" aria-label="Group therapy session with three people in a bright living room" style="background:linear-gradient(120deg,#e8e6e1,#c9c3b8 50%,#8c8a78)"></div>
  <div class="body">
    <h3>Emergency Mental Help</h3>
    <p>Lorem ipsum dolor sit amet, consectetur adipiscing sed do eiusmod tempor incididunt ut labore et dolore magna aliqua. Ut enim ad minim veniamcommodo...</p>
    <a class="link">MORE OPTIONS FOR EMERGENCY MENTAL HELP</a>
  </div>
</article>
<article class="card" style="left:615px">
  <div class="img" role="img" aria-label="Two women smiling on a sofa holding a chat sign" style="background:linear-gradient(180deg,#dfe6e8,#b9cbd0 55%,#3f6e73)"></div>
  <span class="abs" style="left:181px;top:24px;width:104px;height:104px;border-radius:50%;background:var(--green);border:5px solid #fff"></span>
  <div class="body">
    <h3>Smart Chatline</h3>
    <p>Lorem ipsum dolor sit amet, consectetur adipiscing sed do eiusmod tempor incididunt ut labore et dolore magna aliqua. Ut enim ad minim veniamcommodo...</p>
    <a class="link">05X-XXXXXXX</a>
  </div>
</article>

<!-- therapists -->
<svg class="abs" style="left:0;top:2080px" width="1200" height="700" viewBox="0 0 1200 700">
  <path d="M0 0C80 120 200 60 330 70 470 80 560 40 700 80 860 120 1000 130 1200 180V560C1050 600 950 520 860 520 720 520 640 560 560 520 470 470 380 600 250 590 150 585 80 560 0 520Z" fill="var(--green)"/>
  <path d="M0 60C120 130 260 60 330 160 260 250 80 200 0 300Z" fill="#5caf4c" opacity=".5"/>
  <path d="M740 520C840 480 960 510 990 560 1010 620 960 700 900 715 820 730 720 680 720 620 718 570 720 535 740 520Z" fill="#a9c6e3" opacity=".75"/>
</svg>
<div class="abs" role="img" aria-label="Three smiling therapists standing together" style="left:481px;top:2165px;width:719px;height:582px;background:linear-gradient(90deg,rgba(60,60,60,.0),#5a5f66 20%,#8c96a3 50%,#3c3f45 80%,rgba(40,40,40,.0));clip-path:path('M40 430C40 220 120 70 230 70 300 70 330 140 340 180 380 40 480 10 520 20 600 30 650 120 660 180 700 90 760 80 719 80V582H520C420 560 300 520 180 470 100 450 60 450 40 430Z')"></div>
<div class="feature on-green" style="left:93px;top:2344px">
  <h3>Therapists</h3>
  <p>Lorem ipsum dolor sit amet, consectetur adipiscing elit, sed do eiusmod tempor incididunt ut labore et dolore magna aliqua. Ut enim ad minim veniam, quis nostrud exercitation ullamco laboris nisi ut aliquip ex ea commodo consequat.</p>
  <a class="link">FIND THERAPISTS</a>
</div>

<!-- organizations -->
<div class="photo-circle" role="img" aria-label="Doctors and nurse reviewing documents together" style="left:141px;top:2755px;width:490px;height:490px;background:radial-gradient(circle at 50% 45%,#e9eef2,#9fc0dc 45%,#5b7a99 75%,#d9dde1)"></div>
<div class="feature" style="left:669px;top:2928px;width:380px">
  <h3>Organizations</h3>
  <p>Lorem ipsum dolor sit amet, consectetur adipiscing elit, sed do eiusmod tempor incididunt ut labore et dolore magna aliqua. Ut enim ad minim veniam, quis nostrud exercitation ullamco laboris nisi ut aliquip ex ea commodo consequat.</p>
  <a class="link">FIND ORGANIZATIONS</a>
</div>

<!-- videos -->
<div class="photo-circle" role="img" aria-label="Man in red sweater holding his head during a therapy session" style="left:568px;top:3188px;width:490px;height:490px;background:radial-gradient(circle at 50% 45%,#c0392b,#8e3a33 35%,#a8a6a3 60%,#d7d6d4)"></div>
<div class="play"><svg width="22" height="24" viewBox="0 0 22 24"><path d="M2 2l18 10L2 22z" fill="#fff"/></svg></div>
<div class="feature" style="left:141px;top:3363px">
  <h3>Videos</h3>
  <p>Lorem ipsum dolor sit amet, consectetur adipiscing elit, sed do eiusmod tempor incididunt ut labore et dolore magna aliqua. Ut enim ad minim veniam, quis nostrud exercitation ullamco laboris nisi ut aliquip ex ea commodo consequat.</p>
  <a class="link">VIDEO LIBRARY</a>
</div>

<!-- footer -->
<svg class="footer-bg" width="1200" height="356" viewBox="0 0 1200 356">
  <path d="M0 80C150 10 300 30 440 90 600 160 800 140 980 70 1080 30 1160 20 1200 30V356H0Z" fill="var(--blue)"/>
  <path d="M440 90C600 160 800 140 980 70 1080 30 1160 20 1200 30V48C1150 40 1080 55 990 95 800 175 600 185 430 110Z" fill="#fff" opacity=".25"/>
  <path d="M0 150C120 120 240 160 280 250 300 300 260 340 200 356H0Z" fill="#2a7cca" opacity=".6"/>
</svg>
<div class="footer-brand"><span class="dot"></span>TovaLamishpacha</div>
<div class="footer-line"></div>
<div class="footer-copy">TovaLamishpacha - Organization for Mental Health ©2023</div>
<div class="footer-links"><span>Privacy Policy</span><span>|</span><span>Terms</span></div>
<div class="chat-float"><svg width="20" height="20" viewBox="0 0 20 20"><path d="M6 3l2.5 3-1.5 1.5c.8 1.8 2.2 3.2 4 4L12.5 10 15.5 12.5 14 15C8.5 14.5 4.5 10.5 4 5z" fill="#fff"/></svg></div>

</body>
</html>
```